LASIK low price tagline project

Seeking a creative person to create a catchy tag line, with art, for our LASIK laser vision correction pricing. We wish to lowering our price by half, and keep it that low. The tag line I came up with myself is "Great LASIK value. Low LASIK Price". But it's not too catchy. Also, please know it's illegal to imply surgical results; so, we cannot say something like Great LASIK Outcome at a Low LASIK Price. This campaign would be used in our newsletters and as an online campaign. Our brand standards are attached.

Target Market(s)

Creative designers, wordsmiths, marketing mavens

Industry/Entity Type

Health And Wellness

Font styles to use
Sans Serif

Requirements
Must have
• Short catchy tag line
Nice to have
• illiteration or catchy, memorable phrase
Should not have
• Cannot guarantee a surgical result. Cannot imply a surgical result.

```html
<!DOCTYPE html>
<html lang="en">
<head>
<meta charset="utf-8">
<title>LASIK – High in Value. Low in Price.</title>
<link rel="stylesheet" href="https://fonts.googleapis.com/css2?family=Source+Sans+3:wght@400;600;700&display=swap">
<style>
  :root {
    --white: #ffffff;
    --blush: #efcfd3;
    --blush-soft: #ecc0c6;
    --rose: #e4abb2;
    --rose-deep: #e6a6ae;
    --brick: #cd5f69;
    --slate: #b3b3b3;
    --slate-rose: #a58d90;
    --ink: #111111;
    --photo-light: #d9b8aa;
    --photo-mid: #9c7a6c;
    --photo-dark: #3e3230;
  }
  * { box-sizing: border-box; margin: 0; padding: 0; }
  html, body { width: 1200px; height: 628px; overflow: hidden; background: var(--white); }
  .ad {
    position: relative;
    width: 1200px;
    height: 628px;
    overflow: hidden;
    background: var(--white);
    font-family: "Source Sans 3", "Helvetica Neue", Arial, sans-serif;
    color: var(--ink);
  }
  .block { position: absolute; }

  .band-top        { left: 0;   top: 0;   width: 1200px; height: 17px;  background: var(--blush-soft); }
  .band-top-rose   { left: 202px; top: 0; width: 461px; height: 17px;  background: var(--rose-deep); }
  .rule-left       { left: 0;   top: 50px; width: 202px; height: 13px;  background: var(--brick); }
  .panel-left      { left: 0;   top: 105px; width: 462px; height: 523px; background: var(--blush); }
  .panel-center    { left: 202px; top: 17px; width: 461px; height: 505px; background: var(--blush); }
  .panel-overlap   { left: 202px; top: 105px; width: 260px; height: 417px; background: var(--rose); }
  .tile-grey       { left: 679px; top: 0;   width: 166px; height: 148px; background: var(--slate); }
  .tile-grey-top   { left: 679px; top: 0;   width: 166px; height: 17px;  background: var(--slate-rose); }
  .rule-right      { left: 679px; top: 157px; width: 521px; height: 15px; background: var(--brick); }
  .panel-right     { left: 679px; top: 203px; width: 521px; height: 132px; background: var(--blush); }
  .strip-grey      { left: 679px; top: 360px; width: 73px;  height: 268px; background: var(--slate); }

  .photo {
    left: 752px; top: 330px; width: 448px; height: 298px;
    background: linear-gradient(90deg, var(--photo-light) 0%, var(--photo-mid) 65%, var(--photo-dark) 100%);
  }

  .band-bottom      { left: 0;   top: 550px; width: 1200px; height: 78px; background: var(--blush-soft); opacity: .92; }
  .band-bottom-rose { left: 0;   top: 550px; width: 462px;  height: 78px; background: var(--rose-deep); }
  .band-bottom-grey { left: 679px; top: 550px; width: 73px; height: 78px; background: var(--slate-rose); }
  .band-bottom-photo{ left: 752px; top: 550px; width: 448px; height: 78px; background: var(--rose); opacity: .45; }

  .brand {
    position: absolute; left: 908px; top: 28px;
    display: flex; align-items: center; gap: 8px;
    white-space: nowrap;
  }
  .brand-mark { width: 54px; height: 54px; background: var(--ink); border-radius: 6px; flex: none; }
  .brand-name { font-weight: 600; font-size: 25px; letter-spacing: -0.5px; color: var(--ink); }
  .contact {
    position: absolute; left: 860px; top: 90px; width: 290px;
    text-align: center; font-size: 18px; line-height: 24px; font-weight: 400;
    white-space: nowrap;
  }
  .contact span { display: block; }

  .eyebrow {
    position: absolute; left: 0; width: 1200px; top: 166px;
    text-align: center; font-weight: 700; font-size: 34px;
  }
  .eyebrow sup { font-size: 20px; vertical-align: 12px; }
  .headline {
    position: absolute; left: 0; width: 1190px; top: 240px;
    text-align: center; font-size: 50px; font-weight: 400; letter-spacing: .3px;
    white-space: nowrap;
  }
  .headline strong { font-weight: 700; }
  .headline .gap { display: inline-block; width: 18px; }

  .site {
    position: absolute; left: 18px; top: 586px;
    font-size: 27px; font-weight: 700; color: var(--white);
    white-space: nowrap;
  }
</style>
</head>
<body>
  <main class="ad">
    <div class="block band-top"></div>
    <div class="block band-top-rose"></div>
    <div class="block rule-left"></div>
    <div class="block panel-left"></div>
    <div class="block panel-center"></div>
    <div class="block panel-overlap"></div>
    <div class="block tile-grey"></div>
    <div class="block tile-grey-top"></div>
    <div class="block rule-right"></div>
    <div class="block panel-right"></div>
    <div class="block strip-grey"></div>
    <div class="block photo" role="img" aria-label="Close-up photograph of a woman's blue eye and brow"></div>
    <div class="block band-bottom"></div>
    <div class="block band-bottom-rose"></div>
    <div class="block band-bottom-grey"></div>
    <div class="block band-bottom-photo"></div>

    <div class="brand">
      <span class="brand-mark"></span>
      <span class="brand-name">Clearview Eye Care</span>
    </div>
    <p class="contact">
      <span>www.ClearviewEye.com/LASIK</span>
      <span>(555) 014-2870</span>
    </p>

    <p class="eyebrow">LASIK<sup>®</sup></p>
    <h1 class="headline"><strong>HIGH</strong> IN <strong>VALUE.</strong><span class="gap"></span><strong>LOW</strong> IN <strong>PRICE.</strong></h1>

    <p class="site">www.ClearviewEye.com</p>
  </main>
</body>
</html>
```